LA's Newest HEMP Facial Oil and Body Oil Packaging Project

We need a packaging concept for a Hemp based facial oil and body oil. We need label design for the bottle and carton graphics. I am attaching a few reference photos. The target demographic is women between 17-35 year old. Products need to be able to stand out in crowded stores with clear calls to action.
1oz Dropper Bottle with Unit Carton - Hemp Facial Oil
4oz PET Bottle with Unit Carton - Hemp + Rose Facial Oil

```html
<!DOCTYPE html>
<html lang="en">
<head>
<meta charset="utf-8">
<title>Body Oil with Hemp &amp; Rose Petals – Carton</title>
<link href="https://fonts.googleapis.com/css2?family=Arvo&family=Open+Sans:wght@400;600&display=swap" rel="stylesheet">
<style>
  :root {
    --stage: #7b7b7b;
    --paper: #f1f1f1;
    --paper-side: #e6e6e6;
    --ink: #1c1c1c;
    --rule: #444444;
    --leaf: #1f6b2c;
    --copper-dark: #7a3a14;
    --copper-mid: #c0823e;
    --gold-light: #f3d48e;
    --gold-mid: #d6a24b;
  }
  * { box-sizing: border-box; margin: 0; padding: 0; }
  html, body { width: 1200px; height: 894px; overflow: hidden; }
  body {
    background: var(--stage);
    display: flex;
    align-items: center;
    justify-content: center;
    font-family: "Arvo", serif;
    color: var(--ink);
  }
  .carton { display: flex; height: 790px; }
  .panel { position: relative; height: 100%; display: flex; flex-direction: column; }
  .panel--front { width: 430px; background: var(--paper); }
  .panel--side { width: 190px; background: var(--paper-side); }
  .metal-band {
    height: 44px;
    background: linear-gradient(90deg, var(--gold-mid), var(--gold-light) 18%, var(--copper-mid) 40%, var(--copper-dark) 58%, var(--gold-light) 80%, var(--copper-mid));
    border-top: 4px solid var(--paper);
    border-bottom: 4px solid var(--paper);
    box-shadow: inset 0 6px 0 rgba(255,255,255,.25);
  }
  .front-frame {
    position: relative;
    flex: 1;
    margin: 20px 22px;
    border: 1px solid var(--rule);
    outline: 1px solid var(--rule);
    outline-offset: 4px;
    display: flex;
    flex-direction: column;
    align-items: center;
    text-align: center;
  }
  .corner-ornament {
    position: absolute;
    width: 46px; height: 46px;
    background: radial-gradient(circle, #9a9a9a 0%, transparent 70%);
    opacity: .55;
  }
  .corner-ornament--tl { top: -8px; left: -8px; }
  .corner-ornament--tr { top: -8px; right: -8px; }
  .corner-ornament--bl { bottom: -8px; left: -8px; }
  .corner-ornament--br { bottom: -8px; right: -8px; }
  .product-title { font-size: 50px; font-weight: 400; margin-top: 44px; letter-spacing: .5px; }
  .product-with { font-size: 24px; margin-top: 26px; }
  .product-ingredients { font-size: 28px; margin-top: 26px; }
  .title-rule {
    width: 250px; height: 5px; margin-top: 16px;
    border-top: 1px solid var(--rule); border-bottom: 1px solid var(--rule);
  }
  .leaf-art {
    width: 190px; height: 190px; margin-top: 30px;
    border-radius: 50% 50% 8px 8px;
    background: radial-gradient(circle at 50% 45%, var(--leaf) 0%, #2c7d38 55%, rgba(31,107,44,.15) 72%, transparent 75%);
  }
  .use-banner {
    margin-top: 24px;
    width: 240px; height: 42px;
    display: flex; align-items: center; justify-content: center;
    font-family: "Open Sans", sans-serif; font-weight: 600; font-size: 16px;
    color: #2a1606;
    background: linear-gradient(90deg, var(--copper-mid), var(--gold-light) 35%, var(--gold-mid) 70%, var(--copper-mid));
    border: 2px solid #5a2c0e;
  }
  .net-weight { margin-top: auto; margin-bottom: 40px; font-family: "Open Sans", sans-serif; font-size: 17px; }
  .side-copy {
    flex: 1;
    padding: 26px 18px;
    font-family: "Open Sans", sans-serif;
    font-size: 11px;
    line-height: 1.75;
    color: #333;
  }
  .side-copy p + p { margin-top: 120px; }
</style>
</head>
<body>
  <main class="carton">
    <section class="panel panel--front">
      <div class="metal-band"></div>
      <div class="front-frame">
        <span class="corner-ornament corner-ornament--tl" role="img" aria-label="Decorative corner flourish"></span>
        <span class="corner-ornament corner-ornament--tr" role="img" aria-label="Decorative corner flourish"></span>
        <span class="corner-ornament corner-ornament--bl" role="img" aria-label="Decorative corner flourish"></span>
        <span class="corner-ornament corner-ornament--br" role="img" aria-label="Decorative corner flourish"></span>
        <h1 class="product-title">Body Oil</h1>
        <p class="product-with">with</p>
        <p class="product-ingredients">Hemp &amp; Rose Petals</p>
        <div class="title-rule"></div>
        <div class="leaf-art" role="img" aria-label="Green hemp leaf illustration"></div>
        <div class="use-banner">Hair, Nail and Body Oil</div>
        <p class="net-weight">Net Wt. 4 oz.</p>
      </div>
      <div class="metal-band"></div>
    </section>
    <section class="panel panel--side">
      <div class="metal-band"></div>
      <div class="side-copy">
        <p>This light body oil blends cold pressed hemp seed oil with real rose petals to soften skin, tame dry ends and condition nails. Smooth a few drops over damp skin after bathing, or warm between palms and work through the lengths of the hair. Massage a single drop into each cuticle at night. For external use only. Keep away from eyes and store away from direct heat and light.</p>
        <p>Ingredients: hemp seed oil, rose petal extract and vitamin E.</p>
      </div>
      <div class="metal-band"></div>
    </section>
  </main>
</body>
</html>
```